Mental Health care Company in Washington DC

We are a new mental health care services provider in Washington DC. Please look at these sites.
https://marlowbrookpartners.com
https://www.quillstoneinc.com
https://velmarsh-kt.org/
https://www.trivanqx.com
https://www.thelanternofqz.com

```html
<!DOCTYPE html>
<html lang="en">
<head>
<meta charset="utf-8">
<title>Norvale Health Services</title>
<link rel="stylesheet" href="https://fonts.googleapis.com/css2?family=Roboto+Condensed:wght@700&family=Mulish:wght@400;500;600;700&family=Arimo:wght@400&display=swap">
<style>
:root{
  --navy:#0e1f44;
  --teal:#a2d8da;
  --teal-btn:#9fd7d9;
  --orange:#f0a461;
  --coral:#e26b58;
  --slate:#3f6f86;
  --cream:#fdf8f4;
  --mist:#f2f9fa;
  --rule:#b9b9b9;
  --text:#1a1a1a;
}
*{margin:0;padding:0;box-sizing:border-box}
html,body{width:1200px;height:3670px;overflow:hidden;background:#fff}
body{position:relative;font-family:"Mulish",sans-serif;color:var(--navy)}
.abs{position:absolute}
.brand{display:flex;align-items:center;gap:10px;font-family:"Mulish",sans-serif;font-weight:700;font-size:27px;color:var(--navy);white-space:nowrap}
.brand-dot{width:12px;height:12px;border-radius:50%;background:var(--orange)}
.nav{font-size:13.5px;font-weight:600;color:var(--navy)}
.nav span{position:absolute;white-space:nowrap}
.btn{position:absolute;display:flex;align-items:center;justify-content:center;border-radius:22px;font-family:"Mulish",sans-serif;font-weight:600;font-size:15.5px;color:var(--navy);background:var(--teal-btn)}
.btn.orange{background:var(--orange)}
.body-copy{font-family:"Arimo",sans-serif;font-size:12px;line-height:23px;color:var(--text)}
.rule{position:absolute;width:50px;height:2px;background:var(--rule)}
.photo{position:absolute}
.social{display:flex;gap:6px}
.social i{width:23px;height:23px;border-radius:50%;background:var(--teal);display:block}
.topbar{left:645px;top:12px;font-size:12px;font-weight:600;display:flex;align-items:center;gap:8px}
.topbar .tel{color:var(--orange);font-weight:500;font-size:13.5px;display:flex;align-items:center;gap:4px}
.header-line{left:530px;top:38px;width:530px;height:1px;background:#e6e6e6}
.hero{left:0;top:88px;width:1200px;height:494px;background:var(--teal)}
.hero h1{position:absolute;left:142px;top:92px;font-family:"Roboto Condensed",sans-serif;font-weight:700;font-size:58px;line-height:60px;color:var(--navy)}
.hero .info{position:absolute;left:152px;top:340px;font-size:12px;font-weight:500}
.hero .phone{position:absolute;left:150px;top:362px;font-size:21px;font-weight:500;display:flex;align-items:center;gap:8px}
.kicker{font-size:24px;font-weight:500}
.title{font-size:40px;font-weight:500;line-height:44px}
.sub{font-size:16px;font-weight:600;color:var(--navy)}
.specialties{left:0;top:1136px;width:1200px;height:757px;background:var(--cream)}
.svc-title{font-size:13px;font-weight:700;color:var(--text)}
.svc-copy{font-family:"Arimo",sans-serif;font-size:12px;line-height:20px;color:var(--text);margin-top:6px}
.svc-icon{position:absolute;width:58px;height:58px;border-radius:50%;background:#fff;box-shadow:0 4px 12px rgba(0,0,0,.12);display:flex;align-items:center;justify-content:center}
.community{left:0;top:2430px;width:1200px;height:392px;background:var(--mist)}
.contact-box{left:182px;top:3050px;width:834px;height:444px;border:1px solid #f1ddd0}
.details{position:absolute;left:0;top:0;width:418px;height:100%;background:var(--cream)}
.inquiry{position:absolute;left:418px;top:0;width:414px;height:100%;background:var(--mist);border-left:1px solid #cfe7ea}
.panel-title{position:absolute;font-size:21px;font-weight:600}
.c-item{position:absolute;left:36px;display:flex;align-items:center;gap:16px;font-size:13px;font-weight:500;color:var(--text);line-height:21px}
.c-item .dot{width:36px;height:36px;border-radius:50%;background:var(--orange);display:flex;align-items:center;justify-content:center;flex:none}
.field{position:absolute;left:38px;width:338px;border-bottom:1px solid #9aa3ad;font-size:12.5px;font-weight:500;color:var(--text);display:flex;align-items:center;gap:10px;padding-bottom:14px}
.footer-bar{left:0;top:3627px;width:1200px;height:43px;background:var(--orange);display:flex;align-items:center;justify-content:center;font-size:13px;font-weight:500;color:var(--navy)}
</style>
</head>
<body>

<header>
  <div class="abs brand" style="left:142px;top:26px"><span class="brand-dot"></span>Norvale Health Services</div>
  <div class="abs topbar">For More Information Call Us Today
    <span class="tel"><svg width="16" height="16" viewBox="0 0 24 24" fill="none" stroke="#f0a461" stroke-width="1.8"><path d="M5 3h4l2 5-3 2a12 12 0 0 0 6 6l2-3 5 2v4a2 2 0 0 1-2 2A18 18 0 0 1 3 5a2 2 0 0 1 2-2z"/></svg>123.456.7890</span>
    <span class="social"><i></i><i></i></span>
  </div>
  <div class="abs header-line"></div>
  <nav class="abs nav" style="left:0;top:62px">
    <span style="left:522px">Home</span><span style="left:598px">About Us</span><span style="left:697px">Services We Provide</span><span style="left:866px">Employment</span><span style="left:985px">Contact Us</span>
  </nav>
</header>

<section class="abs hero">
  <h1>Invest In Yourself<br>- It Starts With<br>Your Mind</h1>
  <div class="btn orange" style="left:142px;top:285px;width:126px;height:40px">Know More</div>
  <div class="info">For More Information Call Us Today</div>
  <div class="phone"><svg width="26" height="26" viewBox="0 0 24 24" fill="none" stroke="#0e1f44" stroke-width="1.5"><path d="M5 3h4l2 5-3 2a12 12 0 0 0 6 6l2-3 5 2v4a2 2 0 0 1-2 2A18 18 0 0 1 3 5a2 2 0 0 1 2-2z"/><path d="M14 3a7 7 0 0 1 7 7M14 6a4 4 0 0 1 4 4"/></svg>123.456.7890</div>
  <div class="photo" role="img" aria-label="Illustration about mental wellness in coral and slate blue tones" style="left:613px;top:0;width:541px;height:494px;background:linear-gradient(90deg,#d9877a,#8f9aa3)"></div>
</section>

<section>
  <div class="photo" role="img" aria-label="Photo of a therapist taking notes while a client sits in a bright office" style="left:140px;top:663px;width:411px;height:383px;background:linear-gradient(135deg,#e4eaee,#b8c8d4 55%,#6f8aa3)"></div>
  <div class="abs kicker" style="left:598px;top:652px">Welcome to</div>
  <div class="abs title" style="left:598px;top:680px">Norvale Health Services</div>
  <div class="rule" style="left:598px;top:730px"></div>
  <div class="abs sub" style="left:598px;top:744px">Compassionate Mental Health Care in Washington, DC</div>
  <p class="abs body-copy" style="left:598px;top:772px;width:460px">At Norvale Health Services, we believe that mental wellness is essential to living a full and meaningful life. Located in the heart of Washington, DC, our practice is committed to supporting individuals, couples, and families on their journey to emotional well-being.</p>
  <div class="abs sub" style="left:598px;top:878px">Your Partner in Healing &amp; Growth</div>
  <p class="abs body-copy" style="left:598px;top:904px;width:465px">Whether you're navigating anxiety, depression, trauma, relationship challenges, or simply looking for support in life transitions, our team of licensed mental health professionals is here to help. We provide a safe, inclusive, and confidential space where you can feel heard, respected, and empowered to heal</p>
  <div class="btn" style="left:598px;top:1016px;width:128px;height:40px">Know More</div>
</section>

<section class="abs specialties">
  <div class="abs kicker" style="left:0;width:1200px;text-align:center;top:76px">Our Specialties</div>
  <div class="abs title" style="left:0;width:1200px;text-align:center;top:104px">Services We Provide</div>
  <div class="rule" style="left:575px;top:156px"></div>

  <div class="photo" role="img" aria-label="Photo of a smiling woman" style="left:554px;top:186px;width:92px;height:163px;border-radius:46px 46px 0 0;background:linear-gradient(180deg,#a9d3d8,#c9a584)"></div>
  <div class="photo" role="img" aria-label="Photo of a counselling session in warm tones" style="left:392px;top:349px;width:162px;height:91px;border-radius:46px 0 0 46px;background:linear-gradient(90deg,#e8d3c0,#c89a73)"></div>
  <div class="photo" role="img" aria-label="Photo of a support group in soft blue tones" style="left:646px;top:349px;width:162px;height:91px;border-radius:0 46px 46px 0;background:linear-gradient(90deg,#dcecef,#8fbfc6)"></div>
  <div class="photo" role="img" aria-label="Photo of hands held in support" style="left:554px;top:440px;width:92px;height:162px;border-radius:0 0 46px 46px;background:linear-gradient(180deg,#c8b3a1,#8a6048)"></div>

  <div class="abs" style="left:164px;top:224px;width:285px;text-align:right"><div class="svc-title">Individual Therapy</div><div class="svc-copy">Ut wisi enim ad minim veniam, quis nostrud exerci tation ullamcorper suscipit lobortis nisl ut aliquip ex ea commodo consequat.</div></div>
  <div class="abs" style="left:754px;top:220px;width:300px"><div class="svc-title">Couples &amp; Family Counseling</div><div class="svc-copy">Ut wisi enim ad minim veniam, quis nostrud exerci tation ullamcorper suscipit lobortis nisl ut aliquip ex ea commodo consequat.</div></div>
  <div class="abs" style="left:164px;top:469px;width:285px;text-align:right"><div class="svc-title">Psychiarty</div><div class="svc-copy">Ut wisi enim ad minim veniam, quis nostrud exerci tation ullamcorper suscipit lobortis nisl ut aliquip ex ea commodo consequat.</div></div>
  <div class="abs" style="left:754px;top:469px;width:300px"><div class="svc-title">Community Support Services</div><div class="svc-copy">Ut wisi enim ad minim veniam, quis nostrud exerci tation ullamcorper suscipit lobortis nisl ut aliquip ex ea commodo consequat.</div></div>

  <div class="svc-icon" style="left:476px;top:227px"><svg width="30" height="30" viewBox="0 0 30 30" fill="none" stroke="#0e1f44" stroke-width="1.5"><circle cx="9" cy="12" r="3"/><circle cx="21" cy="12" r="3"/><path d="M4 27v-7a4 4 0 0 1 8 0v7M18 27v-7a4 4 0 0 1 8 0v7"/><circle cx="15" cy="5" r="3" stroke="#f0a461"/></svg></div>
  <div class="svc-icon" style="left:676px;top:227px"><svg width="30" height="30" viewBox="0 0 30 30" fill="none" stroke="#0e1f44" stroke-width="1.5"><circle cx="7" cy="13" r="3"/><circle cx="23" cy="13" r="3"/><path d="M2 27v-6a5 5 0 0 1 10 0M18 21a5 5 0 0 1 10 0v6M10 22h10"/><circle cx="15" cy="5" r="3" stroke="#f0a461"/></svg></div>
  <div class="svc-icon" style="left:476px;top:484px"><svg width="30" height="30" viewBox="0 0 30 30" fill="none" stroke="#0e1f44" stroke-width="1.5"><path d="M8 27v-6a10 10 0 1 1 14-3l2 4h-3v4h-5"/><circle cx="14" cy="12" r="4" stroke="#f0a461"/></svg></div>
  <div class="svc-icon" style="left:676px;top:484px"><svg width="30" height="30" viewBox="0 0 30 30" fill="none" stroke="#0e1f44" stroke-width="1.5"><path d="M3 14l5 8v5M27 14l-5 8v5M9 18l4 4M21 18l-4 4"/><circle cx="11" cy="7" r="2.5" stroke="#f0a461"/><circle cx="19" cy="7" r="2.5" stroke="#f0a461"/></svg></div>

  <div class="btn" style="left:551px;top:638px;width:128px;height:40px">Know More</div>
</section>

<section>
  <div class="abs" style="left:141px;top:2018px;font-size:32px;font-weight:500">Take the First Step Today</div>
  <p class="abs body-copy" style="left:141px;top:2070px;width:410px">Seeking support is a sign of strength. If you're ready to begin your journey toward healing, we're here to walk with you every step of the way.</p>
  <div class="abs" style="left:141px;top:2144px;font-size:13.5px;font-weight:600;color:var(--text);line-height:33px">
    <div style="display:flex;align-items:center;gap:16px"><svg width="18" height="18" viewBox="0 0 24 24" fill="none" stroke="#f0a461" stroke-width="1.6"><path d="M5 3h4l2 5-3 2a12 12 0 0 0 6 6l2-3 5 2v4a2 2 0 0 1-2 2A18 18 0 0 1 3 5a2 2 0 0 1 2-2z"/></svg>Call us at 123.456.7890</div>
    <div style="display:flex;align-items:center;gap:16px"><svg width="18" height="18" viewBox="0 0 24 24" fill="none" stroke="#f0a461" stroke-width="1.6"><path d="M12 22s7-7 7-12a7 7 0 0 0-14 0c0 5 7 12 7 12z"/><circle cx="12" cy="10" r="2.5"/></svg>Visit us at : Street Name, City Name, State Zipcode</div>
    <div style="display:flex;align-items:center;gap:16px"><svg width="18" height="18" viewBox="0 0 24 24" fill="none" stroke="#f0a461" stroke-width="1.6"><rect x="3" y="5" width="16" height="15" rx="2"/><path d="M3 10h16M8 3v4M14 3v4"/></svg>Schedule an appointment online</div>
  </div>
  <div class="btn" style="left:141px;top:2253px;width:176px;height:40px">Contact Us Today</div>
  <div class="photo" role="img" aria-label="Photo of a counsellor with a clipboard talking with a young woman on a sofa" style="left:613px;top:1971px;width:445px;height:382px;background:linear-gradient(120deg,#9cb0b8,#d9dee0 45%,#f1ece6 70%,#7a858d)"></div>
</section>

<section class="abs community">
  <div class="photo" role="img" aria-label="Illustration of caregivers assembling a puzzle-piece brain with a heart, framed by pale leaves" style="left:60px;top:78px;width:530px;height:242px;background:linear-gradient(90deg,#d3e9eb,#9fcdd3 50%,#d3e9eb)"></div>
  <div class="abs title" style="left:612px;top:78px">Rooted in Community,<br>Guided by Care</div>
  <p class="abs body-copy" style="left:616px;top:172px;width:432px">As part of the vibrant and diverse DC community, we honor the unique experiences of every individual we serve. Our team brings cultural competence, evidence-based practices, and a deep commitment to mental health equity.</p>
  <div class="btn" style="left:612px;top:272px;width:176px;height:40px">Contact Us Today</div>
</section>

<section>
  <div class="abs title" style="left:0;width:1200px;text-align:center;top:2898px">Contact Us</div>
  <div class="rule" style="left:575px;top:2953px"></div>
  <p class="abs body-copy" style="left:170px;top:2973px;width:860px;text-align:center">Have questions or need help getting started? Our team is here to support you. Reach out today — whether you're looking to schedule an appointment, learn more about our services, or simply talk to someone who cares.</p>
  <div class="abs contact-box">
    <div class="details">
      <div class="panel-title" style="left:35px;top:54px">Contact Details</div>
      <div class="rule" style="left:35px;top:88px"></div>
      <p class="abs" style="left:35px;top:112px;width:330px;font-size:11.5px;line-height:22px;color:var(--text)">Every message is confidential, and we're committed to responding promptly.</p>
      <div class="c-item" style="top:180px"><span class="dot"><svg width="16" height="16" viewBox="0 0 24 24" fill="none" stroke="#0e1f44" stroke-width="1.8"><path d="M12 22s7-7 7-12a7 7 0 0 0-14 0c0 5 7 12 7 12z"/><circle cx="12" cy="10" r="2.5"/></svg></span><span>Street Name, City Name<br>State Zipcode</span></div>
      <div class="c-item" style="top:229px"><span class="dot"><svg width="16" height="16" viewBox="0 0 24 24" fill="none" stroke="#0e1f44" stroke-width="1.8"><rect x="3" y="6" width="18" height="13" rx="1"/><path d="M3 7l9 7 9-7"/></svg></span><span>info@brelwynmail.com</span></div>
      <div class="c-item" style="top:278px"><span class="dot"><svg width="16" height="16" viewBox="0 0 24 24" fill="none" stroke="#0e1f44" stroke-width="1.8"><path d="M5 3h4l2 5-3 2a12 12 0 0 0 6 6l2-3 5 2v4a2 2 0 0 1-2 2A18 18 0 0 1 3 5a2 2 0 0 1 2-2z"/></svg></span><span>123-456-7890</span></div>
      <div class="abs" style="left:35px;top:339px;display:flex;align-items:center;gap:8px;font-size:16px;font-weight:600">Follow Us: <span class="social"><i style="width:29px;height:29px;background:var(--navy)"></i><i style="width:29px;height:29px;background:var(--navy)"></i></span></div>
    </div>
    <div class="inquiry">
      <div class="panel-title" style="left:36px;top:54px">Quick Inquiry</div>
      <div class="rule" style="left:36px;top:88px"></div>
      <div class="field" style="top:126px"><svg width="14" height="14" viewBox="0 0 24 24" fill="none" stroke="#f0a461" stroke-width="1.8"><circle cx="12" cy="8" r="4"/><path d="M4 21a8 8 0 0 1 16 0"/></svg>Name</div>
      <div class="field" style="top:174px"><svg width="14" height="14" viewBox="0 0 24 24" fill="none" stroke="#f0a461" stroke-width="1.8"><rect x="3" y="6" width="18" height="13" rx="1"/><path d="M3 7l9 7 9-7"/></svg>Email</div>
      <div class="field" style="top:225px"><svg width="14" height="14" viewBox="0 0 24 24" fill="none" stroke="#f0a461" stroke-width="1.8"><path d="M5 3h4l2 5-3 2a12 12 0 0 0 6 6l2-3 5 2v4a2 2 0 0 1-2 2A18 18 0 0 1 3 5a2 2 0 0 1 2-2z"/></svg>Phone</div>
      <div class="field" style="top:274px;height:52px;align-items:flex-start"><svg width="14" height="14" viewBox="0 0 24 24" fill="none" stroke="#f0a461" stroke-width="1.8"><path d="M4 4h16v12H9l-5 4z"/></svg>Message</div>
      <div class="btn" style="left:47px;top:344px;width:98px;height:37px">Submit</div>
    </div>
  </div>
</section>

<footer>
  <div class="abs brand" style="left:140px;top:3555px"><span class="brand-dot"></span>Norvale Health Services</div>
  <nav class="abs nav" style="left:0;top:3562px">
    <span style="left:522px">Home</span><span style="left:598px">About Us</span><span style="left:697px">Services We Provide</span><span style="left:866px">Employment</span><span style="left:985px">Contact Us</span>
  </nav>
  <div class="abs footer-bar">© 2025. Norvale Health Services.&nbsp; All Rights Reserved.</div>
</footer>

</body>
</html>
```